Coastline Aqua works . needs a business card and logo

We are a new company in Orange County , Ca we specialize in pool and spa repair remodel and equipment upgrade, , we want them to know we are a quality company with integrity and pride in our work , and customers satisfaction is our main priority...

On the front of the card I would like to see an AmericanĀ flag theme .. get creative ( a one of a kind card ) and the back of the card glossy custom pool scape , and some where on the back a small picture of a pool equipment skid , heater pool pump filter custom controls , a vexlor pool products equipment pic

Target Market(s)

Pool and spa repair , system upgrades . Custom back yard controls

Industry/Entity Type

Flag

Contact Information for Business Card

Sent two pics the dark one on the back . Lighter one on the front

Font styles to use
Decorative

Requirements
Must have
• American flag In the writing ...
• A custom pool pic of a backyard on the front and back
Nice to have
• Slogan " splash keepers" .. email addresses
• Bluereefaquaworksxy.com
• Rob@bluereefaquaworksxy.com
• Marlow@bluereefaquaworksxy.com 555.241.7782
• Address... 46217 Larkspur Lane harbor Glen 90000
• Ph# 555.613.2950
Should not have
• Hi Dalia, can you put this pic on the front. Plz ... I think it might look better .... Tnks ....

```html
<!DOCTYPE html>
<html lang="en">
<head>
<meta charset="utf-8">
<title>Coastline Aqua works — Business Card</title>
<link rel="stylesheet" href="https://fonts.googleapis.com/css2?family=Kaushan+Script&family=Courgette&family=Cormorant+Garamond:ital,wght@1,500&display=swap">
<style>
  :root {
    --page-bg: #e6e8ec;
    --card-edge: #1a2a8a;
    --flag-red: #c4162a;
    --flag-white: #f4f4f4;
    --flag-blue: #1c2f86;
    --sky-top: #3e6fb8;
    --sky-mid: #a9c3de;
    --deck-tone: #b8a58c;
    --night-top: #05060c;
    --night-mid: #1a1d2e;
    --pool-glow: #1f3fd0;
    --contact-text: #f2f2f2;
  }
  * { box-sizing: border-box; margin: 0; padding: 0; }
  html, body { width: 1200px; height: 1200px; overflow: hidden; }
  body {
    background: var(--page-bg);
    position: relative;
  }
  .card {
    position: absolute;
    left: 150px;
    width: 900px;
    height: 514px;
    border-radius: 26px;
    border: 3px solid var(--card-edge);
    overflow: hidden;
    box-shadow: 0 6px 18px rgba(0,0,0,0.25);
  }
  .card--front { top: 56px; }
  .card--back { top: 630px; }
  .card svg { display: block; width: 100%; height: 100%; }
  .brand-title { font-family: "Kaushan Script", cursive; }
  .slogan { font-family: "Kaushan Script", cursive; }
  .service-list { font-family: "Courgette", cursive; }
  .contact-lines {
    position: absolute;
    top: 22px;
    left: 0;
    right: 0;
    text-align: center;
    font-family: "Cormorant Garamond", serif;
    font-style: italic;
    font-weight: 500;
    font-size: 29px;
    line-height: 42px;
    color: var(--contact-text);
    text-shadow: 0 1px 3px rgba(0,0,0,0.8);
  }
  .backdrop { position: absolute; inset: 0; }
</style>
</head>
<body>

<section class="card card--front">
  <svg viewBox="0 0 900 514" xmlns="http://www.w3.org/2000/svg">
    <defs>
      <linearGradient id="front-photo-tone" x1="0" y1="0" x2="0" y2="1">
        <stop offset="0" stop-color="var(--sky-top)"/>
        <stop offset="0.45" stop-color="var(--sky-mid)"/>
        <stop offset="0.7" stop-color="var(--deck-tone)"/>
        <stop offset="1" stop-color="#2a3440"/>
      </linearGradient>
    </defs>
    <rect class="front-photo" role="img" aria-label="Photo of a modern seaside villa with an infinity pool, lounge chairs and blue sky" width="900" height="514" fill="url(#front-photo-tone)"/>
    <text class="brand-title" x="450" y="120" text-anchor="middle" font-size="84" fill="var(--flag-blue)">Coastline Aqua works.</text>
    <text class="slogan" x="70" y="200" font-size="50" fill="var(--flag-red)">Splash keepers</text>
    <g class="service-list" font-size="34" text-anchor="middle" stroke="var(--flag-white)" stroke-width="0.8">
      <text x="560" y="290" fill="var(--flag-blue)">• Pool and Spa construction •</text>
      <text x="560" y="335" fill="var(--flag-blue)">• Pool and Spa repairs •</text>
      <text x="560" y="380" fill="var(--flag-blue)">• System Upgrades •</text>
      <text x="560" y="425" fill="var(--flag-red)">• Custom Backyard Controls •</text>
      <text x="560" y="470" fill="var(--flag-red)">• Pool Thermal/Solar •</text>
    </g>
  </svg>
</section>

<section class="card card--back">
  <svg class="backdrop" viewBox="0 0 900 514" xmlns="http://www.w3.org/2000/svg" preserveAspectRatio="none">
    <defs>
      <linearGradient id="back-photo-tone" x1="0" y1="0" x2="0" y2="1">
        <stop offset="0" stop-color="var(--night-top)"/>
        <stop offset="0.5" stop-color="var(--night-mid)"/>
        <stop offset="0.72" stop-color="var(--pool-glow)"/>
        <stop offset="1" stop-color="#0a1450"/>
      </linearGradient>
    </defs>
    <rect class="back-photo" role="img" aria-label="Night photo of a lit backyard pool with arcing water jets and stone walls" width="900" height="514" fill="url(#back-photo-tone)"/>
  </svg>
  <div class="contact-lines">
    <p>Phone: 555.613.2950 / 555.241.7782</p>
    <p>Web: www.Bluereefaquaworksxy.com</p>
    <p>E-Mail: Rob@bluereefaquaworksxy.com</p>
    <p>Marlow@bluereefaquaworksxy.com</p>
    <p>Adress: 46217 Larkspur Lane, Harbor Glen, 90000</p>
  </div>
</section>

</body>
</html>
```